Investment Management Marketing Presentation

We need a PowerPoint presentation to introduce our new company to prospective investment clients. We are a small, new firm but our founders have 25+ years experience. We pursue an active, very different investment approach that has been very successful. Please see the attached Word doc for additional guidance.
Updates

Target Market(s)

Financial institutions, wealthy individuals

Industry/Entity Type

Investment Advisory

Font styles to use
Sans Serif

Colors
3176b5

Requirements
Should not have
• Too many stock photos. Graphic elements are better.

```html
<!DOCTYPE html>
<html lang="en">
<head>
<meta charset="utf-8">
<title>Larkspur Capital – US Small Cap Growth Strategy</title>
<link rel="stylesheet" href="https://fonts.googleapis.com/css2?family=Oswald:wght@500&family=Merriweather:wght@400;700&family=Open+Sans:wght@400;600;700&display=swap">
<style>
:root{
  --blue:#3176b5;
  --blue-deep:#1f5e9e;
  --blue-soft:#6f9fd0;
  --ink:#2c3440;
  --muted:#6b7480;
  --stage-top:#ffffff;
  --stage-bottom:#a8a8a8;
  --night-1:#1d2a4a;
  --night-2:#3a4f78;
  --night-3:#16213a;
}
*{margin:0;padding:0;box-sizing:border-box}
html,body{width:1200px;height:2261px;overflow:hidden}
body{position:relative;background:var(--stage-bottom);font-family:"Open Sans",Arial,sans-serif;color:var(--ink)}
.hero-stage{position:absolute;left:0;top:0;width:1200px;height:807px;background:var(--stage-top)}
.hero-slide{position:absolute;left:170px;top:190px;transform:scale(1.6);transform-origin:0 0;box-shadow:0 6px 20px rgba(0,0,0,.25)}
.slide{position:absolute;width:538px;height:260px;background:#fff;overflow:hidden;box-shadow:0 8px 14px rgba(0,0,0,.28)}
.abs{position:absolute}
.heading{font-family:"Merriweather",Georgia,serif;color:var(--blue-deep);font-weight:400}
.label{font-size:6.5px;font-weight:700;color:var(--blue);text-transform:uppercase;letter-spacing:.2px}
.bullets{list-style:none}
.bullets li{position:relative;padding-left:9px;font-size:5.6px;line-height:1.55;margin-bottom:4px}
.bullets li::before{content:"";position:absolute;left:0;top:3px;width:3.5px;height:3.5px;border-radius:50%;background:var(--blue)}
.footer{position:absolute;left:18px;bottom:12px;font-size:5.5px;color:var(--muted)}
.page-no{position:absolute;right:14px;bottom:9px;width:12px;height:12px;background:var(--blue);color:#fff;font-size:5px;display:flex;align-items:center;justify-content:center;border-radius:1px}
.photo{position:absolute}
.title-sky{left:0;top:0;width:538px;height:260px;background:linear-gradient(180deg,var(--night-1) 0%,var(--night-2) 45%,var(--night-3) 100%)}
.title-band{left:150px;top:104px;width:388px;height:86px;background:rgba(49,118,181,.88)}
.title-main{left:215px;top:114px;font-family:"Oswald",Arial,sans-serif;font-size:21px;color:#fff;letter-spacing:.2px}
.title-sub{right:22px;font-family:"Oswald",Arial,sans-serif;font-size:8.5px;color:#fff;letter-spacing:.4px}
.brand-disc{left:58px;top:72px;width:150px;height:150px;border-radius:50%;background:#fff;border:5px solid var(--night-1);display:flex;flex-direction:column;align-items:center;justify-content:center;text-align:center}
.brand-name{font-family:"Merriweather",Georgia,serif;font-size:13px;color:var(--night-1);line-height:1.25}
.toc-photo{left:30px;top:22px;width:230px;height:230px;border-radius:50%;background:linear-gradient(160deg,#9aa0a7,#5d636a 55%,#3c4148)}
.toc-list{left:328px;top:64px;width:190px;list-style:none}
.toc-list li{display:flex;justify-content:space-between;font-size:5.2px;line-height:9.4px;color:var(--ink)}
.objectives{border-collapse:separate;border-spacing:0 6px;font-size:5.2px;text-align:center}
.objectives th{background:var(--blue);color:#fff;font-weight:700;padding:4px 0;border:1px solid var(--blue)}
.objectives td{border:1px solid var(--blue);padding:4px 2px;color:var(--ink);line-height:1.3}
.step{display:flex;align-items:center;gap:9px;height:18px}
.step-dot{width:18px;height:18px;border-radius:50%;background:var(--blue);display:flex;align-items:center;justify-content:center}
.step-name{font-size:6px;font-weight:700;color:var(--blue);letter-spacing:.2px}
.step-arrow{width:18px;height:14px;display:flex;justify-content:center}
.edge-note{left:78px;top:230px;font-size:5.4px;color:var(--ink)}
.closing-brand{position:absolute;left:720px;top:1935px;width:420px;text-align:center;color:#fff}
.closing-brand .name{font-family:"Merriweather",Georgia,serif;font-size:32px;letter-spacing:2px;line-height:1.2}
.closing-brand .tag{font-family:"Merriweather",Georgia,serif;font-size:11px;letter-spacing:1.5px;margin-top:6px}
</style>
</head>
<body>

<section class="hero-stage">
  <div class="slide hero-slide">
    <div class="photo abs title-sky" role="img" aria-label="Dusk view of a wooden pier stretching across a calm lake toward a castle"></div>
    <div class="abs title-band"></div>
    <div class="abs title-main">US SMALL CAP GROWTH STRATEGY</div>
    <div class="abs title-sub" style="top:146px">DANIEL REYES, CHIEF INVESTMENT OFFICER</div>
    <div class="abs title-sub" style="top:164px">APRIL 2019</div>
    <div class="abs brand-disc"><div class="brand-name">LARKSPUR<br>CAPITAL</div></div>
  </div>
</section>

<!-- Title slide -->
<div class="slide" style="left:35px;top:875px">
  <div class="photo abs title-sky" role="img" aria-label="Dusk view of a wooden pier stretching across a calm lake toward a castle"></div>
  <div class="abs title-band"></div>
  <div class="abs title-main">US SMALL CAP GROWTH STRATEGY</div>
  <div class="abs title-sub" style="top:146px">DANIEL REYES, CHIEF INVESTMENT OFFICER</div>
  <div class="abs title-sub" style="top:164px">APRIL 2019</div>
  <div class="abs brand-disc"><div class="brand-name">LARKSPUR<br>CAPITAL</div></div>
</div>

<!-- Table of contents -->
<div class="slide" style="left:624px;top:875px">
  <svg class="abs" style="left:0;top:0" width="300" height="260">
    <circle cx="68" cy="42" r="20" fill="none" stroke="#9cc3ea" stroke-width="7"/>
  </svg>
  <div class="photo toc-photo" role="img" aria-label="Field of dark umbrellas with one red umbrella standing out"></div>
  <svg class="abs" style="left:0;top:0" width="300" height="260">
    <path d="M180 240 A70 70 0 0 1 240 150" fill="none" stroke="#fff" stroke-width="9"/>
  </svg>
  <div class="abs heading" style="left:328px;top:36px;font-size:14px;color:var(--blue)">Table of Contents</div>
  <ul class="abs toc-list">
    <li><span>Overview</span><span>3</span></li>
    <li><span>Boldly Different</span><span>4</span></li>
    <li><span>Synergy Beyond the Style Box</span><span>5</span></li>
    <li><span>Leverages Two Alpha Drivers</span><span>6</span></li>
    <li><span>Philosophy and Process</span><span>7</span></li>
    <li><span>Bold Performance Objectives</span><span>8</span></li>
    <li><span>Investment Process</span><span>9</span></li>
    <li><span>Data and Screening</span><span>10</span></li>
    <li><span>Research and Analysis</span><span>11</span></li>
    <li><span>Stock Selection</span><span>12</span></li>
    <li><span>Portfolio Construction</span><span>13</span></li>
    <li><span>Monitor, Modify and Sell Discipline</span><span>14</span></li>
    <li><span>Risk Management</span><span>15</span></li>
    <li><span>Why Larkspur</span><span>16</span></li>
    <li><span>Exhibits</span><span>17</span></li>
    <li><span>Team</span><span>18</span></li>
    <li><span>Superior Performance Since 1999</span><span>19</span></li>
  </ul>
  <div class="footer">©2019 Larkspur Capital LLC</div>
  <div class="page-no">02</div>
</div>

<!-- Overview -->
<div class="slide" style="left:35px;top:1218px">
  <svg class="abs" style="left:0;top:0" width="538" height="260">
    <polygon points="0,20 20,32 0,44" fill="var(--blue)"/>
    <polygon points="10,18 24,26 10,34" fill="#9cc3ea"/>
    <polygon points="210,38 216,38 213,43" fill="var(--blue)"/>
    <defs><linearGradient id="desk" x1="0" y1="0" x2="1" y2="1"><stop offset="0" stop-color="#c9d3dc"/><stop offset=".5" stop-color="#7a6a58"/><stop offset="1" stop-color="#3f4a58"/></linearGradient></defs>
    <polygon points="315,248 410,30 510,248" fill="url(#desk)" role="img" aria-label="Overhead view of colleagues shaking hands across a desk with a laptop and papers"/>
    <polygon points="300,252 410,20 525,252" fill="none" stroke="var(--blue)" stroke-width="2"/>
    <polygon points="420,30 450,30 435,48" fill="#c9ccd1"/>
    <polygon points="455,55 490,55 472,80" fill="#b5c9de"/>
    <polygon points="470,125 505,125 488,148" fill="var(--blue)"/>
    <polygon points="270,180 300,180 285,206" fill="#c9ccd1"/>
    <polygon points="290,130 315,145 290,160" fill="var(--blue-soft)"/>
    <polygon points="300,228 318,228 309,244" fill="var(--blue)"/>
  </svg>
  <div class="abs heading" style="left:38px;top:44px;font-size:13px">Larkspur Overview</div>
  <div class="abs" style="left:38px;top:92px;width:250px">
    <div class="label">Who is Larkspur</div>
    <ul class="bullets" style="margin-top:5px">
      <li>Tulsa based emerging US small-cap growth (SCG) active equity manager serving institutional investors</li>
      <li>CIO Mark Ellison has over 25 years experience in fundamental growth investing</li>
    </ul>
    <div class="label" style="margin-top:6px">Why Larkspur</div>
    <ul class="bullets" style="margin-top:5px">
      <li>Investment industry evolution presents a business opportunity</li>
      <li>Institutional demand for actively managed SCG equity</li>
      <li>Proven history high-alpha low correlated returns</li>
    </ul>
  </div>
  <div class="footer">©2019 Larkspur Capital LLC</div>
  <div class="page-no">03</div>
</div>

<!-- Vision 2025 -->
<div class="slide" style="left:624px;top:1218px">
  <div class="photo" style="left:0;top:0;width:125px;height:260px;background:linear-gradient(180deg,#3f7fbf,#2f6aa8 60%,#27609c)" role="img" aria-label="Blue-tinted mountain landscape"></div>
  <div class="abs" style="left:12px;top:12px;width:110px;height:236px;border:1px solid rgba(255,255,255,.7)"></div>
  <div class="photo" style="left:362px;top:2px;width:152px;height:92px;background:linear-gradient(135deg,#d8dde3,#9aa5b1 60%,#5a6470)" role="img" aria-label="Team meeting around a table in a bright office"></div>
  <div class="abs" style="left:372px;top:10px;width:152px;height:98px;border:2px solid var(--blue)"></div>
  <div class="abs heading" style="left:160px;top:56px;font-size:13px;color:var(--ink)">Larkspur 2025</div>
  <div class="abs" style="left:160px;top:100px;width:330px">
    <div class="label">Vision</div>
    <ul class="bullets" style="margin-top:5px;width:230px">
      <li>To advise over $1 billion in assets and be recognized among the best US equity managers</li>
    </ul>
    <div class="label" style="margin-top:4px">Mission</div>
    <ul class="bullets" style="margin-top:5px;width:230px">
      <li>To deliver high-alpha investment returns at low correlation over 3- and 5-year periods</li>
    </ul>
    <div class="label" style="margin-top:4px">Mission</div>
    <div style="display:flex;gap:14px;margin-top:5px">
      <ul class="bullets" style="width:150px">
        <li>Consistent disciplined process</li>
        <li>Facts over forecasts</li>
        <li>Proprietary fundamental equity research</li>
      </ul>
      <ul class="bullets" style="width:170px">
        <li>Concentrated, high conviction names with 90% active share</li>
        <li>Clarity and transparency in communications</li>
        <li>Outstanding client service</li>
      </ul>
    </div>
  </div>
  <div class="page-no">04</div>
</div>

<!-- Boldly Different -->
<div class="slide" style="left:35px;top:1564px">
  <div class="abs" style="left:0;top:0;width:140px;height:132px;background:var(--blue)"></div>
  <div class="photo" style="left:70px;top:0;width:70px;height:132px;background:linear-gradient(135deg,#6e9fd0,#3f7fbf)" role="img" aria-label="Blue-tinted hand reaching forward"></div>
  <div class="abs" style="left:8px;top:10px;width:60px;height:150px;border:1px solid rgba(255,255,255,.8)"></div>
  <div class="photo" style="left:375px;top:0;width:163px;height:260px;background:linear-gradient(160deg,#3a3d42,#16181b 60%,#24272c)" role="img" aria-label="Businessman in a dark suit extending an open hand"></div>
  <div class="abs heading" style="left:78px;top:102px;font-size:12px;color:#fff">Boldly <span style="color:var(--blue-deep)">Different</span></div>
  <div class="abs" style="left:34px;top:150px;width:150px">
    <div class="label">Departing from Benchmarks</div>
    <ul class="bullets" style="margin-top:7px">
      <li>Concentrated and Selective</li>
      <li>High Conviction</li>
      <li>Moderate Turnover</li>
      <li>High Active Share</li>
    </ul>
  </div>
  <div class="abs" style="left:200px;top:150px;width:160px">
    <div class="label">Delivers Superior Performance</div>
    <ul class="bullets" style="margin-top:7px">
      <li>High Alpha</li>
      <li>Higher Sharpe Ratio</li>
      <li>Lower Beta</li>
      <li>Asymmetric Risk Profile</li>
      <li>Low Correlation</li>
    </ul>
  </div>
  <div class="footer">©2019 Larkspur Capital LLC</div>
  <div class="page-no">05</div>
</div>

<!-- Bold Performance Objectives -->
<div class="slide" style="left:624px;top:1564px">
  <div class="photo" style="left:0;top:0;width:190px;height:260px;background:linear-gradient(180deg,#2e6aa8,#4a87c4 50%,#2a609b)" role="img" aria-label="Blue-tinted man working on a laptop"></div>
  <div class="abs" style="left:10px;top:28px;width:190px;height:220px;border:1px solid rgba(255,255,255,.75)"></div>
  <svg class="abs" style="left:190px;top:40px" width="20" height="16"><polygon points="0,14 10,0 18,14" fill="var(--blue)"/></svg>
  <svg class="abs" style="left:493px;top:46px" width="10" height="8"><polygon points="0,0 8,0 4,7" fill="var(--blue)"/></svg>
  <div class="abs heading" style="left:212px;top:42px;font-size:12.5px;font-weight:700;color:var(--ink)">Bold Performance Objectives</div>
  <table class="abs objectives" style="left:214px;top:70px;width:286px">
    <tr><th style="width:33%">VALUE</th><th style="width:33%">MEASURE</th><th>OBJECTIVE</th></tr>
    <tr><td>Total Return</td><td>Annualized return (net)</td><td>3% &gt; SCG Index</td></tr>
    <tr><td>Risk (Volatility)</td><td>Annualized standard deviation<br>Beta</td><td>&lt;= SCG Index<br>&lt; 1.0</td></tr>
    <tr><td>Risk-Adjusted Return</td><td>Alpha Sharpe Ratio</td><td>&gt; 3%<br>&gt; SCG Index</td></tr>
    <tr><td>Diversification Contribution</td><td>R² to SCG Index</td><td>0.20 &lt; SCG Index</td></tr>
    <tr><td>Consistency</td><td>3- and 60-month total return<br>36- and 60-month alpha</td><td>75% of periods &gt; SCG Index<br>75% of periods &gt; 0</td></tr>
  </table>
  <div class="page-no">08</div>
</div>

<!-- Investment Process -->
<div class="slide" style="left:35px;top:1909px">
  <svg class="abs" style="left:0;top:0" width="538" height="260">
    <polygon points="4,14 24,4 24,24" fill="var(--blue)"/>
    <polygon points="18,2 34,2 26,14" fill="#9cc3ea"/>
    <polygon points="40,10 52,10 46,18" fill="var(--blue)"/>
    <defs><linearGradient id="tower" x1="0" y1="0" x2="0" y2="1"><stop offset="0" stop-color="#7aa7d8"/><stop offset=".6" stop-color="#4d7fb6"/><stop offset="1" stop-color="#2a4f7e"/></linearGradient></defs>
    <polygon points="60,188 116,44 172,188" fill="url(#tower)" role="img" aria-label="City skyline at dusk with a lit skyscraper at center"/>
    <polygon points="28,44 220,44 124,222" fill="none" stroke="#1c1f24" stroke-width="2.2"/>
    <polygon points="538,146 538,184 508,184" fill="var(--blue-soft)"/>
    <polygon points="500,222 528,222 514,238" fill="#c9ccd1"/>
  </svg>
  <div class="abs heading" style="left:272px;top:20px;font-size:13px;font-weight:700;color:var(--ink)">Investment Process</div>
  <div class="abs" style="left:272px;top:44px;width:200px;height:1px;background:var(--blue)"></div>
  <div class="abs" style="left:282px;top:58px">
    <div class="step"><div class="step-dot"><svg width="9" height="9"><rect x="1" y="1" width="7" height="7" fill="none" stroke="#fff" stroke-width="1"/></svg></div><div class="step-name">DATA AND SCREENING</div></div>
    <div class="step-arrow"><svg width="6" height="14"><line x1="3" y1="1" x2="3" y2="10" stroke="var(--blue)" stroke-width="1"/><polygon points="0,9 6,9 3,13" fill="var(--blue)"/></svg></div>
    <div class="step"><div class="step-dot"><svg width="9" height="9"><circle cx="4" cy="4" r="2.8" fill="none" stroke="#fff" stroke-width="1"/><line x1="6" y1="6" x2="8.5" y2="8.5" stroke="#fff" stroke-width="1"/></svg></div><div class="step-name">RESEARCH AND ANALYSIS</div></div>
    <div class="step-arrow"><svg width="6" height="14"><line x1="3" y1="1" x2="3" y2="10" stroke="var(--blue)" stroke-width="1"/><polygon points="0,9 6,9 3,13" fill="var(--blue)"/></svg></div>
    <div class="step"><div class="step-dot"><svg width="9" height="9"><rect x="1" y="5" width="2" height="3" fill="#fff"/><rect x="4" y="3" width="2" height="5" fill="#fff"/><rect x="7" y="1" width="1.5" height="7" fill="#fff"/></svg></div><div class="step-name">PORTFOLIO &nbsp;CONSTRUCTION</div></div>
    <div class="step-arrow"><svg width="6" height="14"><line x1="3" y1="1" x2="3" y2="10" stroke="var(--blue)" stroke-width="1"/><polygon points="0,9 6,9 3,13" fill="var(--blue)"/></svg></div>
    <div class="step"><div class="step-dot"><svg width="9" height="9"><polyline points="1,7 3.5,4 5.5,6 8,2" fill="none" stroke="#fff" stroke-width="1"/></svg></div><div class="step-name">MONITOR, MODIFY AND SELL</div></div>
  </div>
  <div class="abs edge-note"><b style="color:var(--blue)">LARKSPUR EDGE :</b> Concentrated portfolios of companies with accelerating growth rates, solid momentum and high potential returns.</div>
  <div class="footer" style="bottom:6px">©2019 Larkspur Capital LLC</div>
  <div class="page-no">09</div>
</div>

<div class="closing-brand">
  <div class="name">LARKSPUR</div>
  <div class="tag">CAPITAL · A REGISTERED INVESTMENT ADVISOR</div>
</div>

</body>
</html>
```